1. Can you describe what your company does?
-> We at R and P Orvex, we do Tube bending and its subassemblies. We can cater to different materials like Mild Steel, Stainless Steel, Aluminium and other non-ferrous material. We collaborate with our clients to make precise components to meet their industry requirements. At R&P Orvex we cater to smaller batches or high-volume requirements as per project needs.

2. Who are your target customers for the website?
-> Automotive, Road construction, warehouse equipment, Data centers, beverage equipment industry, electronics products manufacturers for making fixtures.
-> customers which require tubes and pipe bending, exhaust pipes, sheet metal parts

3. Do you have an existing domain name / website address?
-> This was an existing site: https://www.randporvex.co.in/industry
-> using design.com I created this: https://kitpage.site/RandPOrvexpvtltd
But I am not very satisfied with the one I have created using design.com

4. In addition to a Home Page, which other pages / sections would you like your website to have:
About Us
Contact Us
Products / Services
Office / Mailing Address
Terms and Conditions

For each of the pages / sections you’d like to have, please provide the text (and images, if available) you would like to include.
-> Can you use the content that I have added on design.com : https://kitpage.site/RandPOrvexpvtltd

5. Which of the below are features and functionalities your website will need:
Image Gallery
Videos
Contact Form

6. Please provide the URLs for the social media profiles you'd like to link to the website.
-> Don't have one yet.

```html
<!DOCTYPE html>
<html lang="en">
<head>
<meta charset="utf-8">
<title>R and P Orvex — Tube Bending &amp; Forming</title>
<link rel="stylesheet" href="https://fonts.googleapis.com/css2?family=Poppins:wght@400;500;600;700&display=swap">
<style>
:root{
  --blue:#2b56a4;
  --blue-dark:#1f4590;
  --ink:#1f2227;
  --text:#3b3f45;
  --muted:#6c7077;
  --light:#f3f3f3;
  --grey:#8b8e92;
  --white:#ffffff;
}
*{box-sizing:border-box;margin:0;padding:0}
html,body{width:1200px;height:4066px;overflow:hidden}
body{position:relative;background:var(--white);font-family:'Poppins',sans-serif;color:var(--text)}
.abs{position:absolute}
.btn{position:absolute;display:flex;align-items:center;justify-content:center;gap:7px;background:var(--blue);color:var(--white);font-weight:600;font-size:12.5px;border-radius:22px;letter-spacing:.2px;text-decoration:none}
.btn .dot{width:12px;height:12px;border-radius:50%;background:var(--white);position:relative}
.btn .dot::after{content:"";position:absolute;left:4px;top:3px;border-left:5px solid var(--blue);border-top:3px solid transparent;border-bottom:3px solid transparent;width:0;height:0}
.call{position:absolute;display:flex;align-items:center;gap:10px}
.call .ring{width:44px;height:44px;border-radius:50%;background:var(--white);box-shadow:0 2px 10px rgba(0,0,0,.12);display:flex;align-items:center;justify-content:center}
.call small{display:block;font-size:12px;color:var(--ink)}
.call strong{display:block;font-size:16px;color:var(--blue);font-weight:600}
.photo{position:absolute}

/* header */
.site-header{position:absolute;left:0;top:0;width:1200px;height:133px;background:var(--white);z-index:3}
.brand-badge{position:absolute;left:107px;top:-60px;width:184px;height:242px;border-radius:0 0 92px 92px;background:var(--white);border-bottom:4px solid var(--blue);display:flex;align-items:flex-end;justify-content:center;padding-bottom:34px;z-index:4}
.brand-badge span{font-size:16px;color:var(--blue);font-weight:400}
.brand-badge i{position:absolute;top:82px;left:62px;width:60px;height:60px;border-radius:50%;border:3px solid var(--blue)}
.main-nav{position:absolute;top:93px;left:0;width:1200px}
.main-nav a{position:absolute;font-size:13px;font-weight:600;color:var(--ink);text-decoration:none}
.main-nav a.active{color:var(--blue);border-bottom:2px solid var(--blue);padding-bottom:2px}

/* hero */
.hero{position:absolute;left:0;top:133px;width:1200px;height:602px;overflow:hidden}
.hero .photo{left:0;top:0;width:1200px;height:602px;background:
  radial-gradient(ellipse 260px 200px at 230px 260px,rgba(214,170,40,.85),rgba(214,170,40,0) 70%),
  radial-gradient(ellipse 420px 240px at 820px 470px,rgba(20,20,22,.95),rgba(20,20,22,0) 75%),
  radial-gradient(ellipse 300px 200px at 1050px 200px,rgba(150,160,165,.9),rgba(150,160,165,0) 75%),
  linear-gradient(180deg,#8f9397 0%,#6d6c66 45%,#3e3c39 100%)}
.hero-title{position:absolute;left:0;top:160px;width:1200px;text-align:center;color:var(--white);font-size:44px;font-weight:600;line-height:53px;letter-spacing:1px}
.hero-text{position:absolute;left:270px;top:276px;width:660px;text-align:center;color:var(--white);font-size:19.5px;font-weight:500;line-height:28px}
.hero-arrow{position:absolute;top:252px;width:34px;height:34px;border-radius:50%;background:var(--white);display:flex;align-items:center;justify-content:center}
.dots{position:absolute;display:flex;gap:12px}
.dots i{width:13px;height:13px;border-radius:50%;border:2px solid var(--white)}
.dots i.on{background:var(--white)}

/* headings */
.heading{position:absolute;left:0;width:1200px;text-align:center;color:var(--ink);font-weight:600;font-size:38px;line-height:44px}
.heading .u{position:relative;display:inline-block}
.heading .u::after{content:"";position:absolute;left:0;right:0;bottom:-6px;height:4px;background:var(--blue)}

/* intro */
.intro-text{position:absolute;left:150px;top:948px;width:900px;text-align:center;font-size:15.5px;line-height:24px;color:var(--text)}
.intro-text p+p{margin-top:11px}

/* services */
.services{position:absolute;left:0;top:1255px;width:1200px;height:1164px;background:var(--light);overflow:hidden}
.svc-card{position:absolute;top:190px;width:286px;height:466px;background:var(--white);border-radius:143px;box-shadow:0 4px 16px rgba(0,0,0,.08);text-align:center}
.svc-card .photo{left:14px;top:16px;width:257px;height:257px;border-radius:50%}
.svc-card h3{position:absolute;top:290px;left:0;width:100%;font-size:15.5px;font-weight:600;color:var(--ink)}
.svc-card p{position:absolute;top:318px;left:26px;width:234px;font-size:14px;line-height:21px;color:var(--text)}
.svc-card .go{position:absolute;top:399px;left:127px;width:32px;height:32px;border-radius:50%;border:1.5px solid #c9d3e6;display:flex;align-items:center;justify-content:center}
.svc-card .go.on{background:var(--blue);border-color:var(--blue)}
.side-arrow{position:absolute;top:320px}
.prod{position:absolute;top:799px;width:197px;text-align:center}
.prod .ring{width:197px;height:197px;border-radius:50%;border:6px solid rgba(255,255,255,.35);background:var(--white);overflow:hidden;position:relative}
.prod .photo{left:8px;top:8px;width:169px;height:169px;border-radius:50%}
.prod span{display:inline-block;margin-top:22px;color:var(--white);font-size:16px;font-weight:600}
.prod.active .ring{border-color:#c7cbd2}
.prod.active span{border-bottom:2px solid var(--white);padding-bottom:2px}

/* gallery */
.gallery .photo{border-radius:8px}

/* contact */
.contact{position:absolute;left:0;top:3290px;width:1200px;height:441px}
.field{position:absolute;left:210px;width:382px;height:46px;border-radius:23px;background:var(--white);display:flex;align-items:center}
.field .ic{width:50px;height:100%;display:flex;align-items:center;justify-content:center;border-right:1px solid #e1e3e6}
.field span{padding-left:14px;font-size:14.5px;color:var(--ink)}
.message{position:absolute;left:606px;top:133px;width:384px;height:166px;border-radius:22px;background:var(--white)}
.message .ic{position:absolute;left:18px;top:20px}
.message span{position:absolute;left:63px;top:17px;font-size:14.5px;color:var(--ink)}

/* footer */
.site-footer{position:absolute;left:0;top:3731px;width:1200px;height:335px;background:var(--white)}
.foot-brand{position:absolute;left:134px;top:84px;width:165px;height:170px;text-align:center}
.foot-brand i{display:block;margin:0 auto;width:100px;height:100px;border-radius:50%;border:3px solid var(--blue)}
.foot-brand span{display:block;margin-top:34px;font-size:20px;color:var(--blue)}
.foot-col{position:absolute;top:70px}
.foot-col h4{font-size:15px;font-weight:600;color:var(--ink);position:relative;padding-bottom:8px}
.foot-col h4::after{content:"";position:absolute;left:0;bottom:0;width:36px;height:2px;background:var(--blue)}
.foot-col ul{list-style:none;margin-top:12px}
.foot-col li{font-size:12.5px;line-height:26.5px;color:var(--text)}
.info{display:flex;gap:14px;font-size:12.5px;line-height:20px;color:var(--text);margin-top:12px}
.info .ic{width:26px;height:26px;border-radius:50%;background:#e9eef7;flex:none;display:flex;align-items:center;justify-content:center}
.copyright{position:absolute;top:298px;left:0;width:1200px;text-align:center;font-size:11.5px;color:var(--text)}
.social{position:absolute;top:289px;width:34px;height:34px;border-radius:50%;border:1.5px solid #c9d3e6;display:flex;align-items:center;justify-content:center}
.social::after{content:"";width:10px;height:10px;border-radius:50%;background:var(--blue)}
.social.on{background:var(--blue);border-color:var(--blue)}
.social.on::after{background:var(--white)}
</style>
</head>
<body>

<header class="site-header">
  <div class="brand-badge"><i></i><span>R and P Orvex</span></div>
  <a class="btn" style="left:700px;top:28px;width:152px;height:41px">GET IN TOUCH <span class="dot"></span></a>
  <div class="call" style="left:874px;top:26px">
    <div class="ring"><svg width="20" height="20" viewBox="0 0 24 24"><path d="M6.6 10.8a15 15 0 0 0 6.6 6.6l2.2-2.2a1 1 0 0 1 1-.25 11.4 11.4 0 0 0 3.6.57 1 1 0 0 1 1 1V20a1 1 0 0 1-1 1A17 17 0 0 1 3 4a1 1 0 0 1 1-1h3.5a1 1 0 0 1 1 1c0 1.25.2 2.45.57 3.57a1 1 0 0 1-.25 1z" fill="none" stroke="#8b8e92" stroke-width="1.5"/></svg></div>
    <div><small>Call Us:</small><strong>+91-9812345670</strong></div>
  </div>
  <nav class="main-nav">
    <a class="active" style="left:392px">HOME</a>
    <a style="left:456px">ABOUT US</a>
    <a style="left:546px">OUR SERVICES</a>
    <a style="left:666px">INDUSTRIES WE SERVE</a>
    <a style="left:838px">OUR PRODUCTS</a>
    <a style="left:968px">CONTACT US</a>
  </nav>
</header>

<section class="hero">
  <div class="photo" role="img" aria-label="Large black steel pipes at a road construction site with a yellow excavator behind"></div>
  <div class="abs" style="left:0;top:0;width:1200px;height:602px;background:rgba(0,0,0,.2)"></div>
  <h1 class="hero-title">ENGINEERING FLOW,<br>FORMING FUTURE</h1>
  <p class="hero-text">R and P Orvex was founded in 2018 and since then, we have grown to become a leading provider of tube bending and forming services in the industry.</p>
  <a class="btn" style="left:523px;top:390px;width:152px;height:40px">CONTACT US <span class="dot"></span></a>
  <div class="hero-arrow" style="left:56px"><svg width="12" height="12" viewBox="0 0 12 12"><path d="M8 1 3 6l5 5" fill="none" stroke="#1f2227" stroke-width="2"/></svg></div>
  <div class="hero-arrow" style="left:1109px"><svg width="12" height="12" viewBox="0 0 12 12"><path d="M4 1l5 5-5 5" fill="none" stroke="#1f2227" stroke-width="2"/></svg></div>
  <svg class="abs" style="left:0;top:0" width="1200" height="602" viewBox="0 0 1200 602">
    <path d="M0 465 C300 620 650 640 1200 458 L1200 602 L0 602 Z" fill="#ffffff"/>
    <path d="M0 465 C300 620 650 640 1200 458" fill="none" stroke="#2b56a4" stroke-width="10"/>
  </svg>
  <div class="dots" style="left:554px;top:555px"><i></i><i class="on"></i><i></i><i></i></div>
</section>

<h2 class="heading" style="top:831px">R&amp;P ORVEX IS A PERFECT FIT FOR YOUR<br><span class="u">TUBE BENDING</span> NEEDS!</h2>
<div class="intro-text">
  <p>At R&amp;P Orvex, we specialize in precision tube bending and subassembly manufacturing, delivering expert solutions across a diverse range of materials including mild steel, stainless steel, aluminum, and other non-ferrous metals. We partner closely with our clients to engineer precise components that meet exacting industry standards.</p>
  <p>Whether your project requires small-batch prototyping or high-volume production runs, our experienced engineering team works efficiently to enhance product quality, streamline manufacturing processes, and reduce overall costs. "We provide complete solutions for your complex challenges."</p>
</div>
<a class="btn" style="left:430px;top:1133px;width:153px;height:41px">LEARN MORE <span class="dot"></span></a>
<div class="call" style="left:592px;top:1132px">
  <div class="ring"><svg width="20" height="20" viewBox="0 0 24 24"><path d="M6.6 10.8a15 15 0 0 0 6.6 6.6l2.2-2.2a1 1 0 0 1 1-.25 11.4 11.4 0 0 0 3.6.57 1 1 0 0 1 1 1V20a1 1 0 0 1-1 1A17 17 0 0 1 3 4a1 1 0 0 1 1-1h3.5a1 1 0 0 1 1 1c0 1.25.2 2.45.57 3.57a1 1 0 0 1-.25 1z" fill="none" stroke="#8b8e92" stroke-width="1.5"/></svg></div>
  <div><small>Call Us:</small><strong>+91-9812345670</strong></div>
</div>

<section class="services">
  <svg class="abs" style="left:0;top:0" width="1200" height="1164" viewBox="0 0 1200 1164">
    <path d="M0 435 C250 620 950 620 1200 435 L1200 1164 L0 1164 Z" fill="#2b56a4"/>
  </svg>
  <h2 class="heading" style="top:97px"><span class="u">OUR SERVICES</span></h2>
  <svg class="side-arrow" style="left:74px" width="38" height="24" viewBox="0 0 38 24"><path d="M36 12H3M13 2 3 12l10 10" fill="none" stroke="#55595f" stroke-width="2"/></svg>
  <svg class="side-arrow" style="left:1088px" width="38" height="24" viewBox="0 0 38 24"><path d="M2 12h33M25 2l10 10-10 10" fill="none" stroke="#55595f" stroke-width="2"/></svg>

  <article class="svc-card" style="left:144px">
    <div class="photo" role="img" aria-label="Bent stainless steel tubes lying on a grey surface" style="background:radial-gradient(circle at 35% 35%,#e2e3e4 0%,#a9acaf 40%,#6f7377 80%,#55585c 100%)"></div>
    <h3>TUBE AND PIPE BENDING</h3>
    <p>We specialize in Tube and Pipe Bending We handle a variety of industrial projects</p>
    <div class="go"><svg width="14" height="10" viewBox="0 0 14 10"><path d="M1 5h11M8 1l4 4-4 4" fill="none" stroke="#2b56a4" stroke-width="1.5"/></svg></div>
  </article>
  <article class="svc-card" style="left:457px">
    <div class="photo" role="img" aria-label="Formed tube ends in steel and copper on a white background" style="background:radial-gradient(circle at 50% 40%,#ffffff 0%,#eeeeee 45%,#b9bcc0 75%,#8a6a55 100%)"></div>
    <h3>TUBE END FORMING</h3>
    <p>Our tube end forming service is second to none, providing precision and customization</p>
    <div class="go on"><svg width="14" height="10" viewBox="0 0 14 10"><path d="M1 5h11M8 1l4 4-4 4" fill="none" stroke="#ffffff" stroke-width="1.5"/></svg></div>
  </article>
  <article class="svc-card" style="left:770px">
    <div class="photo" role="img" aria-label="Insulated S-shaped exhaust pipe section" style="background:radial-gradient(circle at 50% 50%,#f0efe9 0%,#dedcd4 55%,#c9c6bb 80%,#e7e7e7 100%)"></div>
    <h3>THERMAL INSULATION</h3>
    <p>We offer comprehensive automotive insulation solutions, including Thermal Insulation</p>
    <div class="go"><svg width="14" height="10" viewBox="0 0 14 10"><path d="M1 5h11M8 1l4 4-4 4" fill="none" stroke="#2b56a4" stroke-width="1.5"/></svg></div>
  </article>

  <h2 class="heading" style="top:716px;color:#ffffff"><span class="u">OUR PRODUCTS</span></h2>
  <div class="prod" style="left:148px"><div class="ring"><div class="photo" role="img" aria-label="U-shaped bent steel pipe assembly" style="background:radial-gradient(circle,#ffffff 0%,#f2f2f2 55%,#d7d8da 100%)"></div></div><span>EXPANDING</span></div>
  <div class="prod" style="left:385px"><div class="ring"><div class="photo" role="img" aria-label="Cylindrical steel silencer body" style="background:radial-gradient(circle,#ffffff 0%,#e6e7e8 45%,#f4f4f4 100%)"></div></div><span>EXPANDING</span></div>
  <div class="prod active" style="left:619px"><div class="ring"><div class="photo" role="img" aria-label="Welded tubular steel frame stand" style="background:radial-gradient(circle,#ffffff 0%,#f3f3f3 60%,#e2e2e2 100%)"></div></div><span>EXPANDING</span></div>
  <div class="prod" style="left:856px"><div class="ring"><div class="photo" role="img" aria-label="Exhaust flex pipe being machined in a workshop" style="background:radial-gradient(circle at 50% 55%,#c9c4bc 0%,#8a7d6e 35%,#4d4a48 70%,#2c2c2e 100%)"></div></div><span>EXPANDING</span></div>
  <div class="dots" style="left:554px;top:1085px"><i></i><i class="on"></i><i></i><i></i></div>
</section>

<section class="gallery">
  <h2 class="heading" style="top:2508px"><span class="u">OUR GALLERY</span></h2>
  <div class="photo" role="img" aria-label="Coiled stainless steel pipework" style="left:144px;top:2594px;width:448px;height:263px;background:radial-gradient(ellipse at 55% 50%,#f1f2f3 0%,#b9bdc1 35%,#858a8f 65%,#d4d6d8 100%)"></div>
  <div class="photo" role="img" aria-label="Video of an operator at a tube bending machine" style="left:608px;top:2594px;width:448px;height:263px;background:radial-gradient(ellipse at 40% 55%,#6b7078 0%,#3d4displayed 0%,#2a2c30 60%,#1b1c1f 100%),linear-gradient(120deg,#2f3236,#5a5d61 55%,#393b3e)">
    <svg class="abs" style="left:204px;top:111px" width="40" height="40" viewBox="0 0 40 40"><circle cx="20" cy="20" r="19" fill="#ffffff" opacity=".9"/><path d="M16 12l12 8-12 8z" fill="#2f3236"/></svg>
  </div>
  <div class="photo" role="img" aria-label="Industrial steel piping with valves" style="left:144px;top:2872px;width:295px;height:231px;background:radial-gradient(ellipse at 35% 65%,#8a6a3c 0%,#8a8780 35%,#c7c8c6 75%,#e0e0de 100%)"></div>
  <div class="photo" role="img" aria-label="Yellow CNC tube bending machine in a factory" style="left:453px;top:2872px;width:294px;height:231px;background:radial-gradient(ellipse at 45% 75%,#e2b520 0%,#8f7a2a 30%,#45586a 60%,#6f8797 100%)"></div>
  <div class="photo" role="img" aria-label="Bent pipe on a precision machining bed" style="left:761px;top:2872px;width:295px;height:231px;background:radial-gradient(ellipse at 75% 15%,#e9a08a 0%,#d9c7cf 30%,#e6e6e9 55%,#7d8089 100%)"></div>
  <a class="btn" style="left:503px;top:3142px;width:194px;height:42px">VIEW MORE WORKS <span class="dot"></span></a>
</section>

<section class="contact">
  <svg class="abs" style="left:0;top:0" width="1200" height="441" viewBox="0 0 1200 441">
    <path d="M0 105 C300 -10 900 -10 1200 105 L1200 441 L0 441 Z" fill="#8b8e92"/>
    <path d="M0 105 C300 -10 900 -10 1200 105" fill="none" stroke="#2b56a4" stroke-width="8"/>
  </svg>
  <h2 class="heading" style="top:53px;color:#ffffff"><span class="u">GET IN TOUCH</span></h2>
  <div class="field" style="top:133px"><div class="ic"><svg width="14" height="14" viewBox="0 0 14 14"><circle cx="7" cy="4" r="3" fill="#9a9ea4"/><path d="M1 14c0-4 3-6 6-6s6 2 6 6z" fill="#9a9ea4"/></svg></div><span>Your Name</span></div>
  <div class="field" style="top:195px"><div class="ic"><svg width="14" height="14" viewBox="0 0 24 24"><path d="M6.6 10.8a15 15 0 0 0 6.6 6.6l2.2-2.2a1 1 0 0 1 1-.25 11.4 11.4 0 0 0 3.6.57 1 1 0 0 1 1 1V20a1 1 0 0 1-1 1A17 17 0 0 1 3 4a1 1 0 0 1 1-1h3.5a1 1 0 0 1 1 1c0 1.25.2 2.45.57 3.57a1 1 0 0 1-.25 1z" fill="#9a9ea4"/></svg></div><span>Email</span></div>
  <div class="field" style="top:257px"><div class="ic"><svg width="15" height="12" viewBox="0 0 15 12"><rect width="15" height="12" rx="1.5" fill="#9a9ea4"/><path d="M1 2l6.5 5L14 2" fill="none" stroke="#fff" stroke-width="1.2"/></svg></div><span>Phone</span></div>
  <div class="message"><svg class="ic" width="18" height="14" viewBox="0 0 18 14"><ellipse cx="8" cy="6" rx="8" ry="5.5" fill="#9a9ea4"/><path d="M3 10l-2 4 5-2z" fill="#9a9ea4"/></svg><span>Your Message</span></div>
  <a class="btn" style="left:516px;top:332px;width:168px;height:41px">SEND MESSAGE <span class="dot"></span></a>
</section>

<footer class="site-footer">
  <div class="foot-brand"><i></i><span>R and P Orvex</span></div>
  <div class="foot-col" style="left:377px">
    <h4>QUICK LINKS</h4>
    <ul><li>Home</li><li>About Us</li><li>Our Services</li><li>Industries We Serve</li><li>Our Products</li><li>Contact Us</li></ul>
  </div>
  <div class="foot-col" style="left:576px">
    <h4>OTHER LINKS</h4>
    <ul><li>Privacy Policy</li><li>Terms and Conditions</li><li>Disclaimer</li></ul>
  </div>
  <div class="foot-col" style="left:802px;width:260px">
    <h4>CONTACT INFO</h4>
    <div class="info" style="margin-top:16px"><span class="ic"><svg width="11" height="11" viewBox="0 0 24 24"><path d="M6.6 10.8a15 15 0 0 0 6.6 6.6l2.2-2.2a1 1 0 0 1 1-.25 11.4 11.4 0 0 0 3.6.57 1 1 0 0 1 1 1V20a1 1 0 0 1-1 1A17 17 0 0 1 3 4a1 1 0 0 1 1-1h3.5a1 1 0 0 1 1 1c0 1.25.2 2.45.57 3.57a1 1 0 0 1-.25 1z" fill="#2b56a4"/></svg></span><span style="padding-top:3px">+91-9812345670</span></div>
    <div class="info"><span class="ic"><svg width="11" height="9" viewBox="0 0 15 12"><rect width="15" height="12" rx="1.5" fill="#2b56a4"/><path d="M1 2l6.5 5L14 2" fill="none" stroke="#fff" stroke-width="1.2"/></svg></span><span style="padding-top:3px">randporvex2013@mailbox.com</span></div>
    <div class="info" style="margin-top:18px"><span class="ic"><svg width="10" height="12" viewBox="0 0 10 14"><path d="M5 0a5 5 0 0 1 5 5c0 4-5 9-5 9S0 9 0 5a5 5 0 0 1 5-5z" fill="#2b56a4"/><circle cx="5" cy="5" r="2" fill="#e9eef7"/></svg></span><span style="padding-top:3px">S12 'K' Block Udyog Nagar<br>Nashik- 422010<br>India</span></div>
  </div>
  <p class="copyright">© 2026 &nbsp;/&nbsp; All Rights Reserved</p>
  <span class="social" style="left:941px" aria-label="Social profile"></span>
  <span class="social on" style="left:982px" aria-label="Social profile"></span>
  <span class="social" style="left:1022px" aria-label="Social profile"></span>
</footer>

</body>
</html>
```